Flyer for swimming pool business

My company is R&T Sunwave Pools. We do pool cleaning and maintenance services. We are entering our second season and want a nice flyer to solicit new business and mail to customers. Our slogan is "When you need your water bright, Call R&T Sunwave Pools tonight!" Maybe some package pricing options? I have a picture I use on the invoices which I have attached, you don't have to use it.
Please be creative, I'm looking for something original to stand out from all the other pool company's flyers in the area.

Please include the following as a list:
Weekly Maintenance & Vacuums
Pool Opening & Closings
Pump Repairs
Tile Cleaning
Acid Washes
Algae Removal
Heater Repair
Liner Repair
Leak Detection
One time clean ups

Last years flyer is attached below but I am looking for something different this year.
Updates

Please incorporate this into the flyer.

Pool Opening & Closings

Pump Repairs

Tile Cleaning

Acid Washes

Algae Removal

Heater Repair

Liner Repair

Leak Detection

One time clean ups

Target Market(s)

upper NY suburbs

Industry/Entity Type

Business

Requirements
Must have
• Our phone number 555-318-2746
water background
our slogan "When you need your water bright, Call R&T Sunwave Pools tonight!
our website www.CallSunwaveNow.example
email: sales@CallSunwaveNow.example

```html
<!DOCTYPE html>
<html lang="en">
<head>
<meta charset="utf-8">
<title>R&amp;T Sunwave Pools – Pool Cleaning Services</title>
<link rel="stylesheet" href="https://fonts.googleapis.com/css2?family=Luckiest+Guy&family=Montserrat:wght@400;500&display=swap">
<style>
  :root {
    --stone: #cbc2b2;
    --stone-dark: #b3a995;
    --stone-line: #9d937f;
    --pool-deep: #1aa3cf;
    --pool-mid: #3fbfe3;
    --pool-edge: #a9e6f6;
    --text-white: #ffffff;
    --text-shadow: rgba(10, 90, 140, 0.55);
    --noodle-pink: #d98aa0;
    --noodle-green: #7fa05a;
    --tone-warm: rgba(240, 214, 170, 0.55);
    --tone-cool: rgba(255, 255, 255, 0.35);
    --tone-red: rgba(228, 81, 45, 0.55);
  }
  html, body {
    margin: 0;
    padding: 0;
    width: 854px;
    height: 1200px;
    overflow: hidden;
    background: var(--stone);
  }
  .flyer {
    position: relative;
    width: 854px;
    height: 1200px;
    background: linear-gradient(135deg, #d3cbbb 0%, var(--stone) 50%, #c3b9a6 100%);
    font-family: "Luckiest Guy", "Arial Black", sans-serif;
    font-weight: 400;
    color: var(--text-white);
    overflow: hidden;
  }
  .coping-frame {
    position: absolute;
    left: 14px; top: 14px;
    width: 824px; height: 1170px;
    border: 2px solid var(--stone-line);
    box-sizing: border-box;
  }
  .coping-title {
    position: absolute;
    top: 40px; left: 0; width: 100%;
    margin: 0;
    text-align: center;
    font-size: 20px;
    letter-spacing: 1px;
    color: var(--stone-dark);
  }
  .pool {
    position: absolute;
    left: 86px; top: 84px;
    width: 684px; height: 1036px;
    border: 10px solid var(--pool-edge);
    box-sizing: border-box;
    background:
      radial-gradient(ellipse at 30% 20%, rgba(255,255,255,0.25), transparent 55%),
      radial-gradient(ellipse at 75% 80%, rgba(255,255,255,0.18), transparent 50%),
      linear-gradient(180deg, var(--pool-mid) 0%, var(--pool-deep) 55%, var(--pool-mid) 100%);
  }
  .txt {
    position: absolute;
    margin: 0;
    white-space: nowrap;
    font-weight: 400;
    text-shadow: 2px 3px 0 var(--text-shadow);
  }
  .centered {
    left: 110px; width: 634px;
    text-align: center;
  }
  .headline {
    top: 148px;
    font-size: 72px;
    line-height: 1;
    letter-spacing: 2px;
  }
  .slogan {
    top: 290px;
    font-size: 23px;
    line-height: 46px;
    letter-spacing: 1px;
  }
  .noodle {
    position: absolute;
    left: 143px;
    width: 580px;
    height: 13px;
    border-radius: 7px;
  }
  .noodle--pink { top: 431px; background: linear-gradient(180deg, #eaa9bb, var(--noodle-pink)); }
  .noodle--green { top: 726px; background: linear-gradient(180deg, #9bbb74, var(--noodle-green)); }
  .phone {
    top: 476px;
    font-size: 40px;
    letter-spacing: 4px;
  }
  .contact-label {
    left: 147px;
    font-size: 18px;
    letter-spacing: 1px;
  }
  .contact-value {
    left: 147px;
    font-size: 31px;
    letter-spacing: 1px;
  }
  .label-web { top: 543px; }
  .value-web { top: 564px; }
  .label-mail { top: 640px; }
  .value-mail { top: 661px; }
  .services {
    position: absolute;
    top: 764px; left: 130px;
    margin: 0; padding: 0;
    list-style: none;
    font-size: 19px;
    line-height: 29.8px;
    letter-spacing: 0.5px;
    white-space: nowrap;
    text-shadow: 2px 2px 0 var(--text-shadow);
  }
  .services li::before { content: "- "; }
  .float-area {
    position: absolute;
    border-radius: 10px;
  }
  .float-area--flower {
    left: 200px; top: 350px; width: 58px; height: 52px;
    background: radial-gradient(ellipse, var(--tone-warm), transparent 70%);
  }
  .float-area--bottles {
    left: 676px; top: 500px; width: 84px; height: 92px;
    background: radial-gradient(ellipse, rgba(200, 170, 80, 0.4), transparent 70%);
  }
  .float-area--ball {
    left: 516px; top: 786px; width: 132px; height: 130px;
    background: radial-gradient(ellipse, var(--tone-cool), transparent 72%);
  }
  .float-area--ring {
    left: 558px; top: 918px; width: 150px; height: 150px;
    background: radial-gradient(ellipse, var(--tone-red), transparent 72%);
  }
  .footer-line {
    position: absolute;
    top: 1136px; left: 0; width: 854px;
    margin: 0;
    text-align: center;
    font-family: "Montserrat", sans-serif;
    font-weight: 400;
    font-size: 15px;
    color: var(--text-white);
    letter-spacing: 0.3px;
  }
</style>
</head>
<body>
<main class="flyer">
  <div class="coping-frame"></div>
  <p class="coping-title">R&amp;T SUNWAVE POOL CLEANING SERVICES</p>

  <div class="pool" role="img" aria-label="Top view of a swimming pool with blue mosaic tiles and water ripples"></div>

  <h1 class="txt centered headline">R&amp;T SUNWAVE</h1>
  <p class="txt centered slogan">When you need your water bright,<br>Call R&amp;T Sunwave Pools tonight!</p>
  <div class="float-area float-area--flower" role="img" aria-label="Flower floating on the water"></div>

  <div class="noodle noodle--pink"></div>

  <p class="txt centered phone">TEL: 555-318-2746</p>
  <div class="float-area float-area--bottles" role="img" aria-label="Two glass bottles floating on the water"></div>

  <p class="txt contact-label label-web">Website:</p>
  <p class="txt contact-value value-web">www.CallSunwaveNow.example</p>
  <p class="txt contact-label label-mail">Email:</p>
  <p class="txt contact-value value-mail">sales@CallSunwaveNow.example</p>

  <div class="noodle noodle--green"></div>

  <ul class="services">
    <li>Weekly Maintenance &amp; Vacuums</li>
    <li>Pool Opening &amp; Closings</li>
    <li>Pump Repairs</li>
    <li>Tile Cleaning</li>
    <li>Acid Washes</li>
    <li>Algae Removal</li>
    <li>Heater Repair</li>
    <li>Liner Repair</li>
    <li>Leak Detection</li>
    <li>One Time Clean Ups</li>
  </ul>

  <div class="float-area float-area--ball" role="img" aria-label="Beach ball floating in the pool"></div>
  <div class="float-area float-area--ring" role="img" aria-label="Life ring floating in the pool"></div>

  <p class="footer-line">MORE INFO: WWW.CALLSUNWAVENOW.EXAMPLE &nbsp;//&nbsp; TEL: 555-318-2746</p>
</main>
</body>
</html>
```